Plumbing Website

Design a simple 4 page website based on our provided logo and sketches. Winning designer should be willing to upgrade as needed (for additional fee). A design that includes SEO features is a plus.
I would like to see Home, , Services, Recent Jobs (set up for pictures), Contact. I like the water dropplet back ground. Please dont put logo in a box. File attached as exaple only, I am looking for a request service now button in the middle that will have a form fill to be emailed to two different addresses,
I would like to see vibrant colors. Examples of sites I like are www.maplewickplumbingandheat.com look also at www.kfv-fernvalleyplumbing.com - this site is too busy but has good seo features.

```html
<!DOCTYPE html>
<html lang="en">
<head>
<meta charset="utf-8">
<title>Ridgecrest Plumbing – Experts in Plumbing</title>
<link rel="stylesheet" href="https://fonts.googleapis.com/css2?family=Signika:wght@400;600&family=Asap+Condensed:wght@400;500&family=Open+Sans:wght@400;700&family=Playfair+Display:wght@700;900&display=swap">
<style>
  :root{
    --water-deep:#0b63b8;
    --water-mid:#2a8ee0;
    --water-light:#6cc0f5;
    --brand-blue:#1565b8;
    --brand-red:#d8171f;
    --red-dark:#a90f15;
    --white:#ffffff;
    --ink:#222222;
    --body-text:#444444;
    --rule:#dddddd;
  }
  *{box-sizing:border-box;margin:0;padding:0}
  html,body{width:1200px;height:1093px;overflow:hidden}
  body{position:relative;font-family:"Asap Condensed",sans-serif;color:var(--ink)}
  .backdrop{position:absolute;inset:0;
    background:radial-gradient(circle at 70% 30%,var(--water-light) 0%,var(--water-mid) 40%,var(--water-deep) 100%)}
  .abs{position:absolute}

  /* header */
  .header-shape{left:0;top:0}
  .brand{left:200px;top:48px;display:flex;align-items:center;gap:10px;
    font-family:"Signika",sans-serif;font-weight:600;font-size:27px;color:var(--brand-blue)}
  .brand .dot{width:18px;height:18px;border-radius:50%;background:var(--brand-red)}
  .location{left:632px;top:32px;display:flex;align-items:center;gap:10px;
    font-family:"Playfair Display",serif;font-weight:700;font-size:15px;color:var(--white)}
  .phone-top{left:838px;top:30px;display:flex;align-items:center;gap:10px;
    font-family:"Open Sans",sans-serif;font-weight:700;font-size:21px;color:var(--white)}
  .main-nav{left:634px;top:81px;width:386px;height:32px;display:flex;border-radius:6px;overflow:hidden;
    background:linear-gradient(var(--brand-red),var(--red-dark));font-family:"Open Sans",sans-serif;font-size:13px}
  .main-nav a{flex:1;display:flex;align-items:center;justify-content:center;color:var(--white);text-decoration:none}
  .main-nav a.current{flex:0 0 89px;background:linear-gradient(#2a85d8,var(--brand-blue))}

  /* hero */
  .hero-title{left:197px;top:192px;font-family:"Playfair Display",serif;font-weight:900;font-size:33px;
    color:var(--brand-red);text-shadow:-2px -2px 0 #fff,2px -2px 0 #fff,-2px 2px 0 #fff,2px 2px 0 #fff,3px 4px 5px rgba(0,0,0,.4)}
  .hero-points{left:197px;top:250px;list-style:none;font-family:"Open Sans",sans-serif;font-weight:700;font-size:16.5px;color:var(--white)}
  .hero-points li{display:flex;align-items:center;gap:10px;height:32px}
  .cta{left:198px;top:368px;width:263px;height:40px;border:2px solid var(--white);border-radius:7px;
    background:linear-gradient(#e52a2f,var(--red-dark));color:var(--white);font-family:"Open Sans",sans-serif;
    font-weight:700;font-size:14px;display:flex;align-items:center;justify-content:center;box-shadow:0 2px 5px rgba(0,0,0,.35)}
  .hero-visual{left:623px;top:142px;width:404px;height:337px;border-radius:8px;
    background:linear-gradient(135deg,#dfe8ef 0%,#8fa4b6 45%,#3d5a78 100%);opacity:.85}

  /* content */
  .content{left:169px;top:480px;width:861px;height:517px;background:var(--white);border-radius:7px}
  .welcome{left:169px;top:496px;width:861px;text-align:center;font-family:"Signika",sans-serif;font-size:26px;color:var(--brand-blue)}
  .welcome strong{font-weight:600}
  .intro{left:185px;top:546px;width:830px;text-align:center;font-size:12.3px;line-height:15px;color:var(--body-text)}
  .intro p{margin-bottom:14px}
  .services{left:181px;top:675px;width:836px;height:216px;display:flex;border-top:1px solid var(--rule);border-bottom:1px solid var(--rule)}
  .service{display:flex;flex-direction:column;align-items:center;text-align:center;padding-top:10px}
  .service:nth-child(1){width:277px}
  .service:nth-child(2){width:292px;border-left:1px solid var(--rule);border-right:1px solid var(--rule)}
  .service:nth-child(3){width:267px}
  .service h2{font-family:"Signika",sans-serif;font-weight:400;font-size:22px;color:var(--brand-blue);height:40px}
  .service svg{height:68px}
  .service p{font-size:12.3px;line-height:15px;color:var(--body-text);width:240px;margin-top:14px;height:52px}
  .more{width:62px;height:22px;border-radius:8px;background:linear-gradient(#e52a2f,var(--red-dark));
    color:var(--white);font-family:"Open Sans",sans-serif;font-weight:700;font-size:10px;display:flex;align-items:center;justify-content:center}
  .reach{left:169px;top:902px;width:861px;text-align:center;font-family:"Signika",sans-serif;font-size:16px;line-height:21px;color:var(--ink)}
  .reach .tel{color:var(--brand-red);font-weight:600;font-size:18px}
  .reach a{color:var(--brand-blue)}
  .sign-off{left:169px;top:961px;width:861px;text-align:center;font-family:"Signika",sans-serif;font-weight:600;font-size:16px}

  /* footer */
  .footer-shape{left:0;top:0}
  .footer-nav{left:182px;top:1030px;font-family:"Open Sans",sans-serif;font-size:13px;color:var(--brand-blue)}
  .footer-nav a{color:var(--brand-blue);text-decoration:none}
  .footer-nav a.current{color:var(--brand-red)}
  .footer-nav span{margin:0 10px}
  .copyright{left:182px;top:1061px;font-family:"Open Sans",sans-serif;font-size:10px;color:#e6f1fb}
  .find-us{left:799px;top:1037px;display:flex;align-items:center;gap:11px;font-family:"Signika",sans-serif;font-size:21px;color:var(--brand-red)}
  .find-us span.social{width:30px;height:30px;border-radius:50%;background:var(--brand-blue)}
  .find-us span.social:nth-child(3){background:var(--water-mid)}
  .find-us span.social:nth-child(4){background:#1a7ab3}
</style>
</head>
<body>
  <div class="backdrop" role="img" aria-label="Blue background covered in water droplets"></div>

  <svg class="abs header-shape" width="1200" height="130" aria-hidden="true">
    <path d="M179 14 H435 Q452 14 460 34 Q472 68 500 68 H1020 Q1030 68 1030 78 V116 Q1030 126 1020 126 H179 Q169 126 169 116 V24 Q169 14 179 14 Z" fill="#fff"/>
  </svg>
  <div class="abs brand"><span class="dot"></span>Ridgecrest Plumbing</div>
  <div class="abs location">
    <svg width="16" height="26" viewBox="0 0 16 26"><path d="M8 0a8 8 0 0 0-8 8c0 6 8 18 8 18s8-12 8-18a8 8 0 0 0-8-8zm0 11a3 3 0 1 1 0-6 3 3 0 0 1 0 6z" fill="#fff"/></svg>
    Alder Bay, Westfield
  </div>
  <div class="abs phone-top">
    <svg width="24" height="28" viewBox="0 0 24 28"><path d="M6 1c2 0 3 1 3 2l1 6c0 1-1 2-3 3 1 4 4 8 7 10 1-2 2-3 3-3l5 2c1 1 1 2 0 4-2 3-5 3-8 1C7 22 2 14 1 7 1 3 3 1 6 1z" fill="#fff"/></svg>
    555-013-4420
  </div>
  <nav class="abs main-nav">
    <a class="current" href="#">Home</a><a href="#">Services</a><a href="#">Recent Jobs</a><a href="#">Contact</a>
  </nav>

  <h1 class="abs hero-title">Experts in Plumbing</h1>
  <ul class="abs hero-points">
    <li><svg width="26" height="22" viewBox="0 0 26 22"><path d="M2 12l7 7L24 2" stroke="#fff" stroke-width="4" fill="none"/></svg>24/7 Emergency Services</li>
    <li><svg width="26" height="22" viewBox="0 0 26 22"><path d="M2 12l7 7L24 2" stroke="#fff" stroke-width="4" fill="none"/></svg>Providing Excellent Customer Service</li>
    <li><svg width="26" height="22" viewBox="0 0 26 22"><path d="M2 12l7 7L24 2" stroke="#fff" stroke-width="4" fill="none"/></svg>World-Class Equipment and Service</li>
  </ul>
  <a class="abs cta" href="#">Click Here for Emergency Plumbing</a>
  <div class="abs hero-visual" role="img" aria-label="Chrome mixer tap with water running from the spout"></div>

  <section class="abs content"></section>
  <h2 class="abs welcome"><strong>Welcome to</strong> Ridgecrest Plumbing</h2>
  <div class="abs intro">
    <p>Ridgecrest Plumbing is the industry leader in the area. We are a Plumbing, Drain Cleaning, and General Engineering contractors, providing excellent customer service and helping homeowners to live more comfortable and healthy lives.</p>
    <p>If you are looking for a Plumber in Alder Valley then call on Ridgecrest Plumbing as your Plumbing Contractor.</p>
    <p>When the water heater bursts or the bathroom is flooding, do you want the best plumber available, or do you want the cheapest? At Ridgecrest Plumbing, we know that the best plumber does world-class work, is fully licensed and insured, is available 24/7 – including during emergencies – and somehow combines world-class equipment and service with world-class affordability.</p>
  </div>

  <div class="abs services">
    <div class="service">
      <h2>Plumbing</h2>
      <svg width="80" height="68" viewBox="0 0 80 68"><rect x="30" y="14" width="14" height="10" fill="#222"/><rect x="22" y="8" width="30" height="7" rx="3" fill="#222"/><path d="M8 30h50q12 0 12 12v6h-14v-6H20q-6 0-6 6v14H4V36q0-6 4-6z" fill="#222"/><rect x="64" y="26" width="12" height="26" rx="3" fill="#222"/></svg>
      <p>We are a full-service plumbing company. Our plumbers are experts at repairing or replacing all types of leaks, faucets, toilets ...</p>
      <a class="more">more</a>
    </div>
    <div class="service">
      <h2>Drain Clining</h2>
      <svg width="80" height="68" viewBox="0 0 80 68"><path d="M12 6h20v12h-8v22q0 14 16 14t16-14V14h-6V6h20v8h-4v26q0 26-26 26T12 40V18h-4V6z" fill="#222"/></svg>
      <p>We have been cleaning drains for almost 20 years. Whether it's a kitchen sink or a main sewer line stoppage, we have cleaned ...</p>
      <a class="more">more</a>
    </div>
    <div class="service">
      <h2>General Engineering</h2>
      <svg width="80" height="68" viewBox="0 0 80 68"><path d="M50 2l18 10-6 10-8-4-4 6 6 4-34 40-12-10 34-36-4-4 6-10z" fill="#222"/></svg>
      <p>What sets us apart, is being a class "A" engineering contractor. On larger projects that require cutting concrete and asphalt ...</p>
      <a class="more">more</a>
    </div>
  </div>

  <div class="abs reach">
    You can reach us at <span class="tel">555-013-4420</span>.<br>
    You can also contact us at our e-mail address: <a href="#">service@ridgecrestplumbing.example</a>
  </div>
  <p class="abs sign-off">We are looking forward to hearing from you!</p>

  <svg class="abs footer-shape" width="1200" height="1093" aria-hidden="true" style="pointer-events:none">
    <path d="M177 1023 H1022 Q1030 1023 1030 1031 V1069 Q1030 1077 1022 1077 H800 Q780 1077 772 1062 Q766 1055 750 1055 H177 Q169 1055 169 1047 V1031 Q169 1023 177 1023 Z" fill="#fff"/>
  </svg>
  <nav class="abs footer-nav">
    <a class="current" href="#">Home</a><span>|</span><a href="#">Services</a><span>|</span><a href="#">Recent Jobs</a><span>|</span><a href="#">Contact</a>
  </nav>
  <p class="abs copyright">Copyright © 2013. All Right Reserved.</p>
  <div class="abs find-us">Find us on <span class="social"></span><span class="social"></span><span class="social"></span></div>
</body>
</html>
```